Create Modern Clean Memorable Home Page

Please visit our current Homepage at www.brelvox.com. We want a fresh fun updated and memorable look. Feel free to use any of our photos if necessary. For more inspiration here are some other ice melt websites to browse:
http://www.quoralt.com/
http://www.pembrith.com/ice-melt/
http://www.globalvendrasalt.com/logistics.html
http://www.halvicsalt.com/
http://www.gubrine.com/
http://www.brinevaultco.com/gallery
http://www.thawfrost.com/products/calcium-chloride/
http://www.pelbranworks.com/dry-products
Updates
I have uploaded the logo
Just a note, we are not looking to simply display the product bags on the homepage. We want the first look at our page to pop and be memorable. We want color and possibly the use of photos with people and or animals and or landscapes to depict the use of the product. Most importantly it should be clean and not busy.
Industry/Entity Type
Logistics
Look and feel
Each slider illustrates characteristics of the customer's brand and the style your logo design should communicate.

```html
<!DOCTYPE html>
<html lang="en">
<head>
<meta charset="utf-8">
<title>Brelvox Seasonal Products</title>
<link rel="stylesheet" href="https://fonts.googleapis.com/css2?family=Oxygen:wght@400;700&family=Arimo:wght@400;700&display=swap">
<style>
:root{
  --navy:#0a2f6b;
  --navy-deep:#062a5c;
  --sky:#0a9fd6;
  --sky-light:#27a9df;
  --page:#f1f1f1;
  --card:#ffffff;
  --line:#d9d9d9;
  --text:#555555;
  --text-dark:#333333;
}
*{box-sizing:border-box;margin:0;padding:0}
html,body{width:1055px;height:1200px;overflow:hidden}
body{background:var(--page);font-family:'Arimo',Arial,sans-serif;color:var(--text);position:relative}
.abs{position:absolute}

.brand{display:flex;align-items:center;gap:8px;color:var(--navy);font-family:'Oxygen',sans-serif;font-weight:400;white-space:nowrap}
.brand-mark{background:var(--navy);flex:none}
.header-brand{left:88px;top:18px;font-size:30px;line-height:1}
.header-brand .brand-mark{width:46px;height:46px}

.contact{right:86px;top:6px;text-align:right;font-family:'Oxygen',sans-serif}
.contact-lead{color:var(--sky);font-size:16px}
.contact-phone{display:flex;align-items:center;justify-content:flex-end;gap:10px;color:var(--navy);font-size:31px;line-height:1.05;margin-top:2px}
.contact-email{color:var(--sky);font-size:13px}

.nav{left:452px;top:84px;width:517px;height:60px;background:var(--navy);border-radius:16px 16px 0 0;display:flex;justify-content:space-between;align-items:flex-start;padding:19px 4px 0;font-family:'Oxygen',sans-serif;font-size:10.2px;white-space:nowrap}
.nav a{color:#fff;text-decoration:none;padding:0 3px;border-right:1px solid rgba(255,255,255,.15);line-height:14px}
.nav a:last-child{border-right:none}

.band{left:0;top:143px;width:1055px;height:360px;background:var(--sky)}

.hero{left:88px;top:130px;width:879px;height:390px;background:#fff;box-shadow:0 1px 4px rgba(0,0,0,.25);padding:5px 4px}
.hero-photo{width:100%;height:100%;background:linear-gradient(160deg,#e9edf2 0%,#c9d0d8 40%,#dfe3e8 70%,#b8bcc2 100%)}
.hero-panel{left:384px;top:204px;width:579px;height:180px;background:rgba(255,255,255,.72)}
.hero-title{left:402px;top:208px;color:var(--sky);font-family:Arial,sans-serif;font-weight:700;font-size:47px;letter-spacing:.5px}
.hero-sub{left:405px;top:278px;width:510px;color:var(--navy);font-family:'Oxygen',sans-serif;font-size:22px;line-height:30px}
.btn-hero{left:405px;top:363px;width:202px;height:40px;background:var(--navy);border-radius:3px;color:#fff;font-family:'Oxygen',sans-serif;font-size:18px;display:flex;align-items:center;justify-content:center;gap:10px}

.card{top:534px;width:286px;height:301px;background:var(--card);border:1px solid var(--line);text-align:center}
.card-shadow{top:836px;width:246px;height:14px;border-radius:50%;background:radial-gradient(ellipse at top,rgba(0,0,0,.28),rgba(0,0,0,0) 70%)}
.card h2{font-family:'Oxygen',sans-serif;font-weight:400;font-size:24px;color:var(--navy);margin-top:8px;letter-spacing:.3px}
.card h2 span{color:var(--sky)}
.mission-photo{margin:16px auto 0;width:238px;height:132px;border:1px solid var(--line);padding:2px;background:#fff}
.mission-photo div{width:100%;height:100%;background:linear-gradient(180deg,#c7d6e6 0%,#e3e8ee 50%,#c6403a 70%,#dfe5ec 100%)}
.card p{font-size:11.4px;line-height:17.6px;color:var(--text)}
.mission-text{margin:10px 24px 0}
.about-text{margin:10px 16px 0;text-align:justify;text-align-last:center}
.btn-read{position:absolute;left:50%;transform:translateX(-50%);top:254px;width:96px;height:32px;border-radius:16px;background:var(--navy);border:2px solid #fff;box-shadow:0 0 0 1px var(--navy);color:#fff;font-size:12px;line-height:28px}

.news{list-style:none;margin-top:11px}
.news li{height:52px;display:flex;align-items:center;text-align:left;background:linear-gradient(90deg,#f3f3f3,#e9e9e9);border-bottom:1px solid #fff}
.news-day{width:40px;text-align:right;color:var(--sky);font-family:'Oxygen',sans-serif;font-size:30px;font-weight:400;letter-spacing:-1px}
.news-mon{writing-mode:vertical-rl;transform:rotate(180deg);font-size:9px;color:#888;margin:0 6px 0 4px;letter-spacing:1px}
.news-text{font-family:'Oxygen',sans-serif;font-size:12.4px;line-height:16px;color:#777;margin-left:10px}

.signup-brand{left:98px;top:886px;font-size:18px}
.signup-brand .brand-mark{width:30px;height:30px}
.divider{left:417px;top:880px;height:50px;border-left:1px dotted #999}
.signup-label{left:448px;top:891px;font-family:'Oxygen',sans-serif;font-size:23px;color:var(--navy)}
.signup-input{left:611px;top:890px;width:229px;height:30px;background:#fff;border:1px solid #ccc;box-shadow:inset 0 1px 3px rgba(0,0,0,.15);font-size:11.5px;font-style:italic;color:#888;padding:8px 8px}
.signup-btn{left:849px;top:890px;width:105px;height:30px;background:var(--sky-light);color:#fff;font-family:'Oxygen',sans-serif;font-size:18px;text-align:center;line-height:30px}
.about{left:99px;top:949px;width:858px;font-size:11.5px;line-height:17.6px;color:var(--text-dark);text-align:justify}
.about a{color:var(--sky);text-decoration:none}
.rule{left:88px;top:1038px;width:880px;height:2px;background:linear-gradient(90deg,transparent,#ddd 20%,#ddd 80%,transparent)}

.footer{left:0;top:1066px;width:1055px;height:134px;background:var(--navy-deep);border-top:4px solid var(--sky)}
.footer-col{top:1088px;list-style:none;font-size:11.5px;line-height:26.4px;color:#fff}
.footer-sep{top:1084px;height:92px;border-left:1px dotted #8aa0c4}
.footer-brand{left:709px;top:1100px;color:#fff;font-size:14.5px;gap:6px}
.footer-brand .brand-mark{background:#fff;width:24px;height:24px}
.footer-legal{left:710px;top:1141px;color:#fff;font-size:11.5px;line-height:16px}
</style>
</head>
<body>

<div class="abs brand header-brand"><span class="brand-mark"></span>Brelvox seasonal products, inc.</div>

<div class="abs contact">
  <div class="contact-lead">For Appointment Call Us Today</div>
  <div class="contact-phone">
    <svg width="24" height="40" viewBox="0 0 24 40" aria-hidden="true"><rect x="1" y="4" width="22" height="34" rx="2" fill="#1a1a1a"/><rect x="4" y="0" width="3" height="6" fill="#1a1a1a"/><rect x="4" y="8" width="16" height="9" fill="#cfd8e3"/><g fill="#cfd8e3"><rect x="4" y="20" width="4" height="3"/><rect x="10" y="20" width="4" height="3"/><rect x="16" y="20" width="4" height="3"/><rect x="4" y="25" width="4" height="3"/><rect x="10" y="25" width="4" height="3"/><rect x="16" y="25" width="4" height="3"/><rect x="4" y="30" width="4" height="3"/><rect x="10" y="30" width="4" height="3"/><rect x="16" y="30" width="4" height="3"/></g></svg>
    <span>555 014 2278</span>
  </div>
  <div class="contact-email">info@brelvoxseasonal.com</div>
</div>

<nav class="abs nav">
  <a href="#">Home</a><a href="#">About Us</a><a href="#">ICE Melters</a><a href="#">Shovels &amp; ICE Choppers</a><a href="#">Salt Spreaders</a><a href="#">Snow Tools</a><a href="#">Contact Us</a>
</nav>

<div class="abs band"></div>
<div class="abs hero"><div class="hero-photo" role="img" aria-label="Photo of a worker in winter gear clearing a snowy street with a snow blower"></div></div>
<div class="abs hero-panel"></div>
<div class="abs hero-title">BRELVOX SEASONAL</div>
<div class="abs hero-sub">Manufacturer &amp; Nationwide Distributor of Ice Melt &amp; Snow Removal Products</div>
<div class="abs btn-hero">More Information
  <svg width="20" height="20" viewBox="0 0 20 20" aria-hidden="true"><circle cx="10" cy="10" r="9" fill="#fff"/><path d="M8 6l5 4-5 4z" fill="#0a2f6b"/></svg>
</div>

<section class="abs card" style="left:86px">
  <h2><span>OUR</span> MISSION</h2>
  <div class="mission-photo"><div role="img" aria-label="Photo of a red compact tractor with a snow blower attachment in the snow"></div></div>
  <p class="mission-text">Brelvox Seasonal Products is one of America's premium producers of snow and ice removal products. Focused purely on rock salt.</p>
  <div class="btn-read">Read More</div>
</section>
<div class="abs card-shadow" style="left:106px"></div>

<section class="abs card" style="left:386px">
  <h2><span>BRELVOX</span> SEASONAL</h2>
  <p class="about-text">Brelvox Seasonal Products is one of America's premium producers of snow and ice removal products. Founded in 1993, Brelvox began as a small redistribution operation focused purely on rock salt. As the of America's premium producers of snow and ice removal products. Founded in 1993, Brelvox began as a small redistribution operation focused purely on rock salt. Founded in 1993, Brelvox began as a small redistribution operation focused purely on rock salt.</p>
  <div class="btn-read">Read More</div>
</section>
<div class="abs card-shadow" style="left:406px"></div>

<section class="abs card" style="left:685px">
  <h2><span>NEWS</span> &amp; EVENT</h2>
  <ul class="news">
    <li><span class="news-day">15</span><span class="news-mon">MAY</span><svg width="6" height="24" viewBox="0 0 6 24" aria-hidden="true"><path d="M1 1l4 11-4 11" fill="none" stroke="#bbb"/></svg><span class="news-text">Lorem ipsum dolor sit dolor sit<br>amet, consectetuer adipiscing elit,</span></li>
    <li><span class="news-day">20</span><span class="news-mon">APR</span><svg width="6" height="24" viewBox="0 0 6 24" aria-hidden="true"><path d="M1 1l4 11-4 11" fill="none" stroke="#bbb"/></svg><span class="news-text">Lorem ipsum dolor sit dolor sit<br>amet, consectetuer adipiscing elit,</span></li>
    <li><span class="news-day">07</span><span class="news-mon">MAR</span><svg width="6" height="24" viewBox="0 0 6 24" aria-hidden="true"><path d="M1 1l4 11-4 11" fill="none" stroke="#bbb"/></svg><span class="news-text">Lorem ipsum dolor sit dolor sit<br>amet, consectetuer adipiscing elit,</span></li>
  </ul>
  <div class="btn-read">Read More</div>
</section>
<div class="abs card-shadow" style="left:705px"></div>

<div class="abs brand signup-brand"><span class="brand-mark"></span>Brelvox seasonal products, inc.</div>
<div class="abs divider"></div>
<div class="abs signup-label">Sign up Email:</div>
<div class="abs signup-input">Email Address</div>
<div class="abs signup-btn">Sign Up</div>

<p class="abs about">Brelvox Seasonal Products is one of America's premium producers of snow and ice removal products. Founded in 1993, Brelvox began as a small redistribution operation focused purely on rock salt. As the of America's premium producers of snow and ice removal products. Founded in 1993, Brelvox began as a small redistribution operation focused purely on rock salt. As the years passed we expanded our product line and began to manufacture our own products. We now produce a full line of snow and ice melters as well as snow shovels and car brushes. snow shovels and car brushes.<a href="#">[Read More]</a>.</p>
<div class="abs rule"></div>

<footer class="abs footer"></footer>
<ul class="abs footer-col" style="left:99px"><li>Quick Start Guide</li><li>About Us</li><li>Contact Us</li><li>Terms And Conditions</li></ul>
<div class="abs footer-sep" style="left:309px"></div>
<ul class="abs footer-col" style="left:395px"><li>Investor Reporting Platform</li><li>Investor And Board Reporting Resources</li><li>Board Reporting Principles</li></ul>
<div class="abs footer-sep" style="left:652px"></div>
<div class="abs brand footer-brand"><span class="brand-mark"></span>Brelvox seasonal products, inc.</div>
<div class="abs footer-legal">2013 BRELVOX ,All Rights Reserved<br>Privacy Policy . Terms of Conditions</div>

</body>
</html>
```